Brenvik Electrical & control letter head

Can you please design me a letter head with the attached logo and the following information

Phone number: 0491857362
Email : Brenvik.Electrical@mailhaven.net
ABN: 71 254 918 604

```html
<!DOCTYPE html>
<html lang="en">
<head>
<meta charset="utf-8">
<title>Brenvik Electrical &amp; control – Letterhead</title>
<link rel="stylesheet" href="https://fonts.googleapis.com/css2?family=Lato:wght@400;700;900&family=Montserrat:wght@400&family=Tangerine:wght@700&display=swap">
<style>
  :root {
    --brand-blue: #1550a8;
    --brand-grey: #666868;
    --ink: #1c1c1c;
    --paper: #ffffff;
    --backdrop: #e4e4e4;
  }
  * { margin: 0; padding: 0; box-sizing: border-box; }
  html, body {
    width: 1200px;
    height: 1079px;
    overflow: hidden;
    background: var(--backdrop);
  }
  .letterhead {
    position: absolute;
    left: 232px;
    top: 20px;
    width: 735px;
    height: 1039px;
    background: var(--paper);
    box-shadow: 0 2px 10px rgba(0,0,0,0.15);
    overflow: hidden;
    font-family: "Lato", sans-serif;
    color: var(--ink);
  }
  .brand-name {
    position: absolute;
    left: 37px;
    top: 58px;
    display: flex;
    align-items: center;
    gap: 8px;
    font-family: "Lato", sans-serif;
    font-weight: 900;
    font-size: 21px;
    color: var(--brand-blue);
    white-space: nowrap;
  }
  .brand-name .brand-square {
    width: 16px;
    height: 16px;
    background: var(--brand-blue);
  }
  .contact-divider {
    position: absolute;
    left: 432px;
    top: 51px;
    width: 1.5px;
    height: 55px;
    background: var(--brand-blue);
  }
  .contact-list {
    position: absolute;
    left: 446px;
    top: 48px;
    list-style: none;
    font-family: "Montserrat", sans-serif;
    font-size: 12px;
    color: var(--ink);
  }
  .contact-list li {
    display: flex;
    align-items: center;
    gap: 4px;
    height: 19px;
  }
  .contact-list li.abn { margin-top: 7px; padding-left: 1px; }
  .contact-list svg { width: 11px; height: 11px; fill: var(--brand-blue); flex: none; }
  .letter-body {
    position: absolute;
    left: 37px;
    top: 237px;
    width: 661px;
    font-size: 14.1px;
    line-height: 16.2px;
  }
  .letter-date { font-size: 14.6px; margin-bottom: 19px; }
  .recipient { font-size: 14.4px; line-height: 17.5px; margin-bottom: 16px; }
  .salutation { font-size: 17.8px; font-weight: 700; margin-top: 12px; margin-bottom: 18px; }
  .letter-body p.copy { text-align: justify; margin-bottom: 16px; }
  .closing { font-size: 14.4px; margin-top: 36px; }
  .signature {
    font-family: "Tangerine", cursive;
    font-weight: 700;
    font-size: 42px;
    line-height: 42px;
    margin-top: 86px;
  }
  .footer-band {
    position: absolute;
    left: 0;
    bottom: 0;
    width: 735px;
    height: 90px;
    background: linear-gradient(180deg, rgba(255,255,255,0) 0%, rgba(102,104,104,0.35) 45%, rgba(21,80,168,0.55) 100%);
  }
</style>
</head>
<body>
  <main class="letterhead">
    <header>
      <div class="brand-name"><span class="brand-square"></span>Brenvik Electrical &amp; control</div>
      <div class="contact-divider"></div>
      <ul class="contact-list">
        <li>
          <svg viewBox="0 0 24 24" aria-hidden="true"><path d="M6.6 10.8a15.2 15.2 0 0 0 6.6 6.6l2.2-2.2a1 1 0 0 1 1-.25 11.4 11.4 0 0 0 3.6.57 1 1 0 0 1 1 1V20a1 1 0 0 1-1 1A17 17 0 0 1 3 4a1 1 0 0 1 1-1h3.5a1 1 0 0 1 1 1c0 1.25.2 2.45.57 3.6a1 1 0 0 1-.25 1z"/></svg>
          0491857362
        </li>
        <li>
          <svg viewBox="0 0 24 24" aria-hidden="true"><path d="M3 5h18a1 1 0 0 1 1 1v12a1 1 0 0 1-1 1H3a1 1 0 0 1-1-1V6a1 1 0 0 1 1-1zm9 7.5L4 7.3V8l8 5.2L20 8v-.7z"/></svg>
          Brenvik.Electrical@mailhaven.net
        </li>
        <li class="abn">ABN: 71 254 918 604</li>
      </ul>
    </header>

    <section class="letter-body">
      <p class="letter-date">January-03-2020</p>
      <p class="recipient">Mr, John Doe<br>President</p>
      <p class="recipient">Link Corppration<br>123 Street Name, Suite# 10<br>City, State, 120023</p>
      <p class="salutation">Dear Mr, John</p>
      <p class="copy">Lorem ipsum dolor sit amet, consectetur adipiscing elit, sed do eiusmod tempor incididunt ut labore et dolore magna aliqua. Ut enim ad minim veniam, quis nostrud exercitation ullamco laboris nisi ut aliquip ex ea commodo consequat. Duis aute irure dolor in reprehenderit in voluptate velit esse cillum dolore eu fugiat nulla pariatur.</p>
      <p class="copy">Lorem ipsum dolor sit amet, consectetur adipiscing elit, sed do eiusmod tempor incididunt ut labore et dolore magna aliqua. Ut enim ad minim veniam, quis nostrud exercitation ullamco laboris nisi ut aliquip ex ea commodo consequat. Duis aute irure dolor in reprehenderit in voluptate velit esse cillum dolore eu fugiat nulla pariatur.</p>
      <p class="copy">Lorem ipsum dolor sit amet, consectetur adipiscing elit, sed do eiusmod tempor incididunt ut labore et dolore magna aliqua. Ut enim ad minim veniam, quis nostrud exercitation ullamco laboris nisi ut aliquip ex ea commodo consequat.</p>
      <p class="copy">Excepteur sint occaecat cupidatat non proident, sunt in culpa qui officia deserunt mollit anim id est laborum. re et dolore magnam aliquam quaerat voluptatem.</p>
      <p class="closing">Regards</p>
      <p class="signature">Michel Smith</p>
    </section>

    <div class="footer-band" role="img" aria-label="Decorative footer band of sweeping grey and blue curves"></div>
  </main>
</body>
</html>
```